Design WORDPRESS Website for E Commerce Business

We are needing a WORDPRESS website for an E Commerce Business that is supplying quailty kids / baby products.

Target Market(s)

Female / Working Mums / New Mums

Industry/Entity Type

Business

Number of Pages Required

1 page

Font styles to use
Sans Serif

Colors
33b8a4
f8fcfd
d3a5cc
f7f1f7
cbcbcb
9d9d9d

```html
<!DOCTYPE html>
<html lang="en">
<head>
<meta charset="utf-8">
<title>Tot &amp; Tumble — Baby &amp; Kids Store</title>
<link rel="stylesheet" href="https://fonts.googleapis.com/css2?family=Open+Sans:wght@400;600;700&family=Playfair+Display:ital,wght@1,600&display=swap">
<style>
:root{
  --teal:#33b8a4;
  --teal-dark:#2f7f74;
  --blue:#2a8fb0;
  --button:#3a8ea8;
  --ink:#222;
  --body:#555;
  --grey:#9d9d9d;
  --grey-box:#8c8c8c;
  --ring:#9fdff2;
  --footer-a:#0a1f2c;
  --footer-b:#075c96;
  --bar:#141c22;
}
*{margin:0;padding:0;box-sizing:border-box}
html,body{width:1200px;height:1200px;overflow:hidden;background:#fff}
body{font-family:"Open Sans",Arial,sans-serif;color:var(--ink);position:relative}
.page{position:absolute;left:385px;top:0;width:430px;height:1200px;background:#fff}
.abs{position:absolute}
.center{text-align:center}

/* header */
.brand{left:57px;top:9px;font-size:10px;font-weight:600;color:var(--teal);line-height:10px;display:flex;align-items:center;gap:3px}
.brand i{display:block;width:7px;height:7px;border-radius:50%;background:var(--grey)}
.info-box{top:6px;height:21px;width:54px;color:#fff;font-size:3.6px;line-height:4.4px;display:flex;align-items:center;justify-content:center;gap:3px;text-align:center}
.info-box.address{left:245px;background:var(--grey-box)}
.info-box.call{left:318px;width:53px;background:#5fc7bf;border:1px solid #b6ebe5}
.info-box b{font-weight:700;font-size:4px}
.nav{left:0;top:33px;width:430px;height:17px;background:var(--teal-dark)}
.nav ul{list-style:none;display:flex;gap:11px;position:absolute;left:57px;top:6px}
.nav li{font-size:3.8px;color:#fff;letter-spacing:.1px}
.search{position:absolute;left:299px;top:4px;width:73px;height:8px;background:#fff;font-size:3.4px;color:#aaa;padding:2px 5px}
.search span{position:absolute;right:0;top:0;width:8px;height:8px;background:#ccc}

/* hero */
.hero{left:0;top:50px;width:430px;height:168px;background:linear-gradient(100deg,#b9a7a5 0%,#8f8488 35%,#b38a92 60%,#8e3a59 80%,#a49aa5 100%)}
.hero-card{left:138px;top:113px;width:153px;height:57px;background:rgba(90,90,95,.72);color:#fff;text-align:center}
.hero-card .kicker{font-size:4.4px;margin-top:13px}
.hero-card h1{font-size:9.5px;font-weight:400;margin-top:2px;letter-spacing:.2px}
.btn{display:inline-block;color:#fff;font-size:3.8px;text-align:center}
.hero-card .btn{background:var(--teal);width:46px;height:9px;line-height:9px;margin-top:5px}

/* welcome */
.welcome{left:0;width:430px;top:244px;font-family:"Playfair Display",Georgia,serif;font-style:italic;font-weight:600;font-size:10.5px;color:var(--teal)}
.intro{left:84px;width:262px;top:267px;font-size:5px;line-height:8px;color:var(--body)}
.pill{border-radius:6px;background:var(--button);height:11px;line-height:11px}
.welcome-btn{left:192px;top:313px;width:45px}

/* services */
.section-title{left:0;width:430px;font-size:9.5px;color:var(--ink)}
.section-title span{color:var(--teal)}
.services-title{top:359px}
.services-sub{left:0;width:430px;top:377px;font-size:5.4px;color:var(--body)}
.service{width:116px}
.service .photo{width:80px;height:80px;margin:0 auto;border-radius:50%;border:1.5px solid var(--ring);background:linear-gradient(135deg,#efe3dd,#c9b29d 55%,#8fb6d6)}
.service h3{font-size:4px;font-weight:600;color:var(--blue);margin-top:7px}
.service p{font-size:4px;line-height:6px;color:var(--body);margin-top:2px}
.service a{display:inline-block;font-size:3.4px;color:var(--teal);border-bottom:1px solid var(--teal);margin-top:5px;text-decoration:none}

/* future products */
.products{left:0;top:705px;width:430px;height:173px;background:linear-gradient(90deg,#8fe2f8 0%,#58b7db 45%,#0e6fa5 80%,#075f99 100%)}
.products h2{position:absolute;top:24px;width:430px;text-align:center;color:#fff;font-size:9.5px;font-weight:400}
.product{top:49px;width:81px;height:105px;background:#fff;box-shadow:0 1px 3px rgba(0,0,0,.25);text-align:center}
.product .pin{position:absolute;left:37px;top:-3px;width:7px;height:7px;border-radius:50%;background:#6d7479}
.product .photo{height:65px;background:linear-gradient(160deg,#f5f2ef,#d9e6ef 60%,#f3c9d8)}
.product h3{font-size:3.4px;color:var(--blue);font-weight:400;margin-top:6px}
.product p{font-size:3.3px;line-height:4.4px;color:#333;margin:4px 6px 0}
.product .pill{position:absolute;left:22px;bottom:-4px;width:37px;height:8px;line-height:8px;font-size:3.4px;border-radius:4px}
.arrow{top:92px;width:18px;height:18px}

/* blogs */
.blogs-title{top:905px;color:var(--blue)}
.blog{width:120px;text-align:center}
.blog .photo{width:88px;height:49px;margin:0 auto;border:1.5px solid #fff;box-shadow:0 1px 4px rgba(0,0,0,.35);background:linear-gradient(120deg,#efe6df,#d9b899 60%,#a9cfe6)}
.blog h3{font-size:3.5px;font-weight:400;color:var(--teal);margin-top:6px}
.blog p{font-size:3.5px;line-height:5px;color:#444;margin-top:1px}
.blog a{display:inline-block;font-size:3.4px;color:var(--blue);border-bottom:1px solid var(--blue);margin-top:5px;text-decoration:none}
.see-more{left:192px;top:1026px;width:45px;height:11px;line-height:11px;background:var(--button)}

/* footer */
.footer{left:0;top:1072px;width:430px;height:112px;background:linear-gradient(90deg,var(--footer-a) 0%,#0a3554 45%,var(--footer-b) 100%);color:#fff}
.footer .col{position:absolute;top:23px}
.footer h4{font-size:5.4px;font-weight:400;margin-bottom:3px}
.footer li{list-style:none;font-size:3.8px;line-height:8.8px;color:#cfe0ea}
.footer .contact{left:299px;top:30px;font-size:3.8px;line-height:4.6px}
.footer .contact .name{font-size:6px;font-weight:600;color:#d4dce2;margin-bottom:10px;display:flex;align-items:center;gap:3px}
.footer .contact .name i{display:block;width:6px;height:6px;background:#9aa6b0;border-radius:50%}
.footer .contact .row{display:flex;gap:4px;margin-bottom:4px}
.footer .contact svg{flex:none}
.bottom-bar{left:0;top:1184px;width:430px;height:16px;background:var(--bar);color:#ddd;font-size:3.6px}
.bottom-bar .copy{position:absolute;left:64px;top:6px}
.bottom-bar .follow{position:absolute;left:356px;top:3px;display:flex;align-items:center;gap:2px}
.bottom-bar .follow i{display:block;width:8px;height:8px;border-radius:50%;border:0.8px solid #ddd}
</style>
</head>
<body>
<div class="page">

  <header>
    <div class="abs brand"><i></i>Tot &amp; Tumble</div>
    <div class="abs info-box address">
      <svg width="5" height="7" viewBox="0 0 10 14"><path d="M5 0a5 5 0 0 1 5 5c0 4-5 9-5 9S0 9 0 5a5 5 0 0 1 5-5z" fill="#fff"/><circle cx="5" cy="5" r="2" fill="#8c8c8c"/></svg>
      <span>14 Willow Lane,<br>Tot &amp; Tumble</span>
    </div>
    <div class="abs info-box call">
      <svg width="6" height="6" viewBox="0 0 12 12"><path d="M2 0l2.5 3L3 4.5a8 8 0 0 0 4.5 4.5L9 7.5 12 10l-2 2C5 12 0 7 0 2z" fill="#fff"/></svg>
      <span>Call Us Now<br><b>555-014-220</b></span>
    </div>
    <nav class="abs nav">
      <ul>
        <li>HOME</li><li>ABOUT US</li><li>OUR SERVICES</li><li>FUTURE PRODUCT</li><li>BLOG</li><li>TESTIMONIALS</li><li>CONTACT US</li>
      </ul>
      <div class="search">Search . . . <span></span></div>
    </nav>
  </header>

  <section>
    <div class="abs hero" role="img" aria-label="Photo of a smiling baby girl playing with building blocks"></div>
    <div class="abs hero-card">
      <p class="kicker">Text of the printing and type setting</p>
      <h1>LOREM IPSUM IS SIMPLY</h1>
      <span class="btn">READ MORE &#10230;</span>
    </div>
  </section>

  <section>
    <h2 class="abs welcome center">Welcome to my site</h2>
    <p class="abs intro center">Lorem Ipsum is simply dummy text of the printing and typesetting industry. Lorem Ipsum has been the industry's standard dummy text ever since the 1500s, when an unknown printer took a galley of type and scrambled it to make a type specimen book. It has sur typesetting industry. Lorem Ipsum has been the 1500s, when an unknown printer took a</p>
    <span class="abs btn pill welcome-btn">READ MORE</span>
  </section>

  <section>
    <h2 class="abs section-title services-title center">OUR <span>SERVICES</span></h2>
    <p class="abs services-sub center">Lorem Ipsum is simply dummy text of the printing and type setting industry.</p>

    <div class="abs service center" style="left:39px;top:402px"><div class="photo" role="img" aria-label="Photo of a mother playing with her child"></div><h3>LOREM IPSUM SIMPLY DUMMY</h3><p>Contrary to popular belief,<br>Lorem Ipsum is not.</p><a>READ MORE</a></div>
    <div class="abs service center" style="left:156px;top:402px"><div class="photo" role="img" aria-label="Photo of a mother and kids with toy glasses"></div><h3>LOREM IPSUM SIMPLY DUMMY</h3><p>Contrary to popular belief,<br>Lorem Ipsum is not.</p><a>READ MORE</a></div>
    <div class="abs service center" style="left:273px;top:402px"><div class="photo" role="img" aria-label="Photo of a toddler with a toy stethoscope and teddy bear"></div><h3>LOREM IPSUM SIMPLY DUMMY</h3><p>Contrary to popular belief,<br>Lorem Ipsum is not.</p><a>READ MORE</a></div>

    <div class="abs service center" style="left:39px;top:545px"><div class="photo" role="img" aria-label="Photo of a baby with a teddy bear"></div><h3>LOREM IPSUM SIMPLY DUMMY</h3><p>Contrary to popular belief,<br>Lorem Ipsum is not.</p><a>READ MORE</a></div>
    <div class="abs service center" style="left:156px;top:545px"><div class="photo" role="img" aria-label="Photo of a toddler building with blocks"></div><h3>LOREM IPSUM SIMPLY DUMMY</h3><p>Contrary to popular belief,<br>Lorem Ipsum is not.</p><a>READ MORE</a></div>
    <div class="abs service center" style="left:273px;top:545px"><div class="photo" role="img" aria-label="Photo of a mother and baby playing with toys"></div><h3>LOREM IPSUM SIMPLY DUMMY</h3><p>Contrary to popular belief,<br>Lorem Ipsum is not.</p><a>READ MORE</a></div>
  </section>

  <section class="abs products">
    <h2>FUTURE PRODUCT</h2>
    <svg class="abs arrow" style="left:35px" viewBox="0 0 18 18"><circle cx="9" cy="9" r="8" fill="none" stroke="#fff" stroke-width="1"/><path d="M10.5 5.5 7 9l3.5 3.5" fill="none" stroke="#fff" stroke-width="1.2"/></svg>
    <svg class="abs arrow" style="left:376px" viewBox="0 0 18 18"><circle cx="9" cy="9" r="8" fill="none" stroke="#fff" stroke-width="1"/><path d="M7.5 5.5 11 9l-3.5 3.5" fill="none" stroke="#fff" stroke-width="1.2"/></svg>

    <div class="abs product" style="left:76px"><span class="pin"></span><div class="photo" role="img" aria-label="Photo of baby bath products and toys in a basket"></div><h3>LOREM IPSUM</h3><p>Consectetur adipiscing elit, sed do eiusmod tempor incididunt ut labore et dolore</p><span class="btn pill">READ MORE</span></div>
    <div class="abs product" style="left:174px"><span class="pin"></span><div class="photo" role="img" aria-label="Photo of folded towels with a rubber duck"></div><h3>LOREM IPSUM</h3><p>Consectetur adipiscing elit, sed do eiusmod tempor incididunt ut labore et dolore</p><span class="btn pill">READ MORE</span></div>
    <div class="abs product" style="left:272px"><span class="pin"></span><div class="photo" role="img" aria-label="Photo of pink towels and bath toys"></div><h3>LOREM IPSUM</h3><p>Consectetur adipiscing elit, sed do eiusmod tempor incididunt ut labore et dolore</p><span class="btn pill">READ MORE</span></div>
  </section>

  <section>
    <h2 class="abs section-title blogs-title center">BLOGS</h2>
    <div class="abs blog" style="left:88px;top:933px"><div class="photo" role="img" aria-label="Photo of a mother and baby with toys"></div><h3>LOREM IPSUM DOLOR SIT AMETCON</h3><p>Lorem ipsum dolor sit amet, consectetur adipiscing<br>elit, sed do eiusmod tempor incididunt</p><a>MORE</a></div>
    <div class="abs blog" style="left:222px;top:933px"><div class="photo" role="img" aria-label="Photo of a toddler sitting in a cardboard box"></div><h3>LOREM IPSUM DOLOR SIT AMETCON</h3><p>Lorem ipsum dolor sit amet, consectetur adipiscing<br>elit, sed do eiusmod tempor incididunt</p><a>MORE</a></div>
    <span class="abs btn see-more">SEE MORE</span>
  </section>

  <footer class="abs footer">
    <div class="col" style="left:57px"><h4>QUICK LINK</h4><ul><li>Home</li><li>About us</li><li>Our Service</li><li>Future Product</li><li>Bolg</li><li>Testimonials</li><li>Contact us</li></ul></div>
    <div class="col" style="left:139px"><h4>OUR SERVICES</h4><ul><li>Consectetur</li><li>Adipiscing elit</li><li>Sed do eiusmod</li><li>Tempor</li><li>Incididunt</li><li>Eiusmod</li><li>Incididunt</li></ul></div>
    <div class="col" style="left:221px"><h4>OTHER LINK</h4><ul><li>Lorem ipsum</li><li>Dolor</li><li>Sit amet</li><li>Consectetur</li><li>Adipiscing</li><li>Elit, sed</li></ul></div>
    <div class="contact abs">
      <div class="name"><i></i>Tot &amp; Tumble</div>
      <div class="row"><svg width="4" height="5" viewBox="0 0 10 14"><path d="M5 0a5 5 0 0 1 5 5c0 4-5 9-5 9S0 9 0 5a5 5 0 0 1 5-5z" fill="#fff"/></svg><span>14 Willow Lane<br>Tot &amp; Tumble, Lorem ipsum 21</span></div>
      <div class="row"><svg width="5" height="4" viewBox="0 0 12 9"><rect x=".5" y=".5" width="11" height="8" fill="none" stroke="#fff"/><path d="M.5.5 6 5l5.5-4.5" fill="none" stroke="#fff"/></svg><span>hello@totandtumble.example</span></div>
      <div class="row" style="margin-top:6px"><svg width="5" height="5" viewBox="0 0 12 12"><path d="M2 0l2.5 3L3 4.5a8 8 0 0 0 4.5 4.5L9 7.5 12 10l-2 2C5 12 0 7 0 2z" fill="#fff"/></svg><span>555-014-221</span></div>
    </div>
  </footer>
  <div class="abs bottom-bar">
    <span class="copy">© 2017 Tot &amp; Tumble. All Rights Reserved.</span>
    <span class="follow">Follow us : <i></i><i></i><i></i><i></i><i></i></span>
  </div>

</div>
</body>
</html>
```